Restaurant promotion flyer

I am selling restaurant thermal paper, pizza boxes, show-up: Order online local delivery, Competitive price,

Target Market(s)

Restaurants

Industry/Entity Type

Restaurant supplies

Requirements
Must have
• The flyers should have headers saying local, the pictures of the items we are selling, and the pricing right next to each of them. The flyer should also be attractive to customers.
Nice to have
• Somethings nice is can show how low and good the pricing is for the products.
Should not have
• Receipt Paper $45.00 3-1/8x230-50 R ; $35.00 3-1/8X119-50 R; Credit Card Paper $26.00 2-1/4x50-100 R; $16.00 2-1/4x85-50 R; Pump Gas Station: $31.00 2-5/16x356-24 R ; $ 25.00 2-5/16X210-24 R;

```html
<!DOCTYPE html>
<html lang="en">
<head>
<meta charset="utf-8">
<title>Local Restaurant Product Selling Flyer</title>
<link rel="stylesheet" href="https://fonts.googleapis.com/css2?family=Montserrat:wght@300;400;700;900&family=Archivo+Black&display=swap">
<style>
  :root {
    --ink: #1b1b1b;
    --brand-red: #961b23;
    --paper: #ffffff;
    --kraft: #c4a57c;
    --kraft-light: #d9c3a2;
    --roll-grey: #dcdcdc;
    --cup-red: #d8222d;
    --shadow: rgba(70, 20, 60, 0.55);
  }
  * { margin: 0; padding: 0; box-sizing: border-box; }
  html, body { width: 848px; height: 1200px; overflow: hidden; background: var(--ink); }
  .flyer {
    position: relative; width: 848px; height: 1200px; overflow: hidden;
    background: linear-gradient(to bottom, var(--ink) 0 648px, var(--brand-red) 648px 100%);
    font-family: "Montserrat", sans-serif;
  }
  .decor { position: absolute; inset: 0; }
  .social { position: absolute; left: 19px; top: 18px; display: flex; gap: 16px; }
  .social span { width: 35px; height: 35px; border-radius: 50%; background: var(--brand-red); display: block; }
  .brand {
    position: absolute; right: 18px; top: 12px; text-align: right;
    font-weight: 700; font-size: 20px; color: var(--paper); line-height: 1.05; letter-spacing: -0.5px;
  }
  .headline { position: absolute; left: 25px; top: 70px; }
  .headline .lead { font-weight: 700; font-size: 56px; color: var(--paper); letter-spacing: -3px; line-height: 1; }
  .headline .product { font-weight: 900; font-size: 96px; color: var(--brand-red); letter-spacing: -2px; line-height: 0.82; margin-top: 8px; }
  .headline .selling { font-weight: 900; font-size: 47px; color: var(--brand-red); letter-spacing: -1.5px; line-height: 1; margin-top: 6px; }
  .headline .tagline { font-weight: 400; font-size: 25px; color: var(--paper); letter-spacing: 1px; margin-top: 4px; }
  .headline .local { font-weight: 700; font-size: 15px; color: var(--brand-red); letter-spacing: 2px; margin-top: 10px; }
  .card {
    position: absolute; background: var(--paper); border-radius: 32px; overflow: hidden;
    box-shadow: 3px 6px 8px var(--shadow);
  }
  .card-title { color: var(--brand-red); font-weight: 400; line-height: 1; letter-spacing: -0.5px; }
  .card-price { font-family: "Archivo Black", sans-serif; color: var(--ink); line-height: 1; }
  .card-price sup { font-family: "Montserrat", sans-serif; font-weight: 400; font-size: 0.5em; vertical-align: 0.9em; }
  .card-body { color: var(--ink); font-weight: 400; text-transform: uppercase; }
  .featured { left: 393px; top: 210px; width: 436px; height: 271px; }
  .featured .card-title { position: absolute; left: 12px; top: 22px; font-family: "Archivo Black", sans-serif; font-size: 29px; letter-spacing: -2px; }
  .featured .card-price { position: absolute; left: 12px; top: 60px; font-family: "Montserrat", sans-serif; font-weight: 500; font-size: 27px; }
  .featured .card-body { position: absolute; left: 12px; top: 98px; width: 190px; font-size: 12.4px; line-height: 15.4px; }
  .featured .photo { position: absolute; left: 207px; top: 14px; width: 229px; height: 257px; background: linear-gradient(160deg, var(--kraft-light), var(--kraft)); }
  .tile { top: 517px; width: 187px; height: 299px; }
  .tile-thermal { left: 70px; }
  .tile-foodbox { left: 331px; }
  .tile-cup { left: 592px; }
  .tile .photo { position: absolute; left: 28px; top: 6px; width: 131px; height: 100px; border-radius: 12px; }
  .tile-thermal .photo { background: linear-gradient(135deg, #f3f3f3, var(--roll-grey)); }
  .tile-foodbox .photo { background: linear-gradient(135deg, var(--kraft-light), var(--kraft)); }
  .tile-cup .photo { background: linear-gradient(90deg, #eeeeee 0 25%, var(--cup-red) 25% 75%, #eeeeee 75%); }
  .tile .card-title { position: absolute; left: 6px; right: 6px; top: 118px; font-size: 20.5px; white-space: nowrap; }
  .tile-cup .card-title { text-align: center; }
  .tile .card-price { position: absolute; left: 6px; top: 144px; font-size: 25px; }
  .tile .card-body { position: absolute; left: 7px; top: 187px; width: 176px; font-size: 10.8px; line-height: 13.7px; }
  .services { position: absolute; left: 140px; top: 840px; width: 568px; height: 211px; background: var(--paper); border-radius: 30px; }
  .services-label {
    position: absolute; left: 152px; top: -1px; width: 265px; height: 41px; border-radius: 50%;
    background: var(--ink); color: var(--paper); font-family: "Archivo Black", sans-serif;
    font-size: 24px; text-align: center; line-height: 40px; word-spacing: 4px;
  }
  .services-list { position: absolute; left: 18px; top: 71px; list-style: none; }
  .services-list li { font-family: "Archivo Black", sans-serif; font-size: 13px; line-height: 20px; color: var(--ink); display: flex; align-items: center; }
  .services-list li::before { content: ""; width: 12px; height: 12px; border-radius: 50%; background: var(--brand-red); margin-right: 1px; }
  .perks { position: absolute; left: 330px; top: 71px; list-style: none; }
  .perks li { font-family: "Archivo Black", sans-serif; font-size: 13px; line-height: 20px; color: var(--brand-red); }
  .contact { position: absolute; left: 7px; top: 1155px; display: flex; align-items: center; gap: 6px; }
  .contact-number { font-family: "Archivo Black", sans-serif; font-size: 17px; color: var(--paper); }
  .cta-icon { position: absolute; left: 642px; top: 1104px; }
  .cta-text { position: absolute; left: 706px; top: 1116px; font-family: "Archivo Black", sans-serif; line-height: 1; }
  .cta-text .small { display: block; color: var(--paper); font-size: 16px; letter-spacing: 1px; }
  .cta-text .big { display: block; color: var(--ink); font-size: 24px; letter-spacing: -1.5px; margin-top: 3px; }
</style>
</head>
<body>
<main class="flyer">
  <svg class="decor" width="848" height="1200" viewBox="0 0 848 1200" aria-hidden="true">
    <ellipse cx="796" cy="30" rx="172" ry="86" fill="none" stroke="var(--brand-red)" stroke-width="3"/>
    <ellipse cx="796" cy="26" rx="148" ry="68" fill="none" stroke="var(--paper)" stroke-width="2"/>
    <circle cx="-174" cy="935" r="251" fill="none" stroke="var(--ink)" stroke-width="4"/>
    <circle cx="786" cy="1123" r="293" fill="none" stroke="var(--ink)" stroke-width="4"/>
  </svg>

  <nav class="social" aria-label="Social channels"><span></span><span></span><span></span></nav>

  <div class="brand">CRUSTLINE<br>SUPPLY</div>

  <header class="headline">
    <h1 class="lead">RESTURENT</h1>
    <div class="product">PRODUCT</div>
    <div class="selling">SELLING</div>
    <p class="tagline">QUALITY WORK FOR YOU</p>
    <p class="local">LOCAL SUPPLIER · ORDER ONLINE</p>
  </header>

  <article class="card featured">
    <h2 class="card-title">PIZZA BOX</h2>
    <div class="card-price">10<sup>$</sup></div>
    <p class="card-body">Lorem ipsum dolor sit amet, consectetur adi-piscing elit, sed do eius-mod tempor incididunt ut labore et dolore magna aliqua. Quis ipsum suspendisse ultrices gravida. Risus commodo viverra maecenas ac-cumsan lacus vel facili-</p>
    <div class="photo" role="img" aria-label="Open brown cardboard pizza box"></div>
  </article>

  <article class="card tile tile-thermal">
    <div class="photo" role="img" aria-label="Roll of white thermal paper"></div>
    <h2 class="card-title">THERMAL PAPER</h2>
    <div class="card-price">5<sup>$</sup></div>
    <p class="card-body">Lorem ipsum dolor sit amet, consectetur adipis-cing elit, sed do eiusmod tempor incididunt ut labore et dolore magna aliqua. Quis ipsum suspen-disse ultrices gravida.</p>
  </article>

  <article class="card tile tile-foodbox">
    <div class="photo" role="img" aria-label="Kraft fast food takeaway boxes"></div>
    <h2 class="card-title">FAST FOOD BOX</h2>
    <div class="card-price">8<sup>$</sup></div>
    <p class="card-body">Lorem ipsum dolor sit amet, consectetur adipis-cing elit, sed do eiusmod tempor incididunt ut labore et dolore magna aliqua. Quis ipsum suspen-disse ultrices gravida.</p>
  </article>

  <article class="card tile tile-cup">
    <div class="photo" role="img" aria-label="Red paper cup between two white foam cups"></div>
    <h2 class="card-title">CUP</h2>
    <div class="card-price">4<sup>$</sup></div>
    <p class="card-body">Lorem ipsum dolor sit amet, consectetur adipis-cing elit, sed do eiusmod tempor incididunt ut labore et dolore magna aliqua. Quis ipsum suspen-disse ultrices gravida.</p>
  </article>

  <section class="services">
    <h2 class="services-label">OUR SERVICES</h2>
    <ul class="services-list">
      <li>PIZZA BOX</li>
      <li>RESTURENT CUP</li>
      <li>THERMAL PAPER</li>
      <li>FAST FOOD BOX</li>
      <li>RESTURENT PILATES</li>
    </ul>
    <ul class="perks">
      <li>ORDER ONLINE</li>
      <li>LOCAL DELIVERY</li>
      <li>COMPETITIVE PRICE</li>
    </ul>
  </section>

  <div class="contact">
    <svg width="21" height="21" viewBox="0 0 21 21" aria-hidden="true">
      <circle cx="10.5" cy="10.5" r="10" fill="var(--ink)"/>
      <path d="M6.5 5.5 L8.6 5.2 L9.6 7.8 L8.4 8.8 Q9.6 11.4 12.2 12.6 L13.2 11.4 L15.8 12.4 L15.5 14.5 Q9 15.5 6.5 5.5 Z" fill="var(--brand-red)"/>
    </svg>
    <span class="contact-number">555-014-2368</span>
  </div>

  <svg class="cta-icon" width="72" height="80" viewBox="0 0 72 80" aria-hidden="true" fill="none" stroke="var(--ink)" stroke-width="3.5" stroke-linecap="round" stroke-linejoin="round">
    <circle cx="28" cy="22" r="14"/>
    <path d="M28 14 V22 L33 26"/>
    <path d="M2 34 V58 H50 L60 6 H70"/>
    <path d="M8 66 H54"/>
    <circle cx="16" cy="73" r="4"/>
    <circle cx="44" cy="73" r="4"/>
  </svg>
  <div class="cta-text"><span class="small">GET OUR</span><span class="big">SERVICES</span></div>
</main>
</body>
</html>
```